Business card for new speaking/consulting business
Carla Venhuizen, CRBTEQ
Bright & Fun-filled
Success Coach, Revenue Cycle Specialist, Speaker
Marrowfield, CO
carla.venhuizen@postvexa.com

```html
<!DOCTYPE html>
<html lang="en">
<head>
<meta charset="utf-8">
<title>Carla Venhuizen — Stationery</title>
<link href="https://fonts.googleapis.com/css2?family=Montserrat:wght@400;600;700&display=swap" rel="stylesheet">
<style>
  :root{
    --bg:#f1f2f3;
    --paper:#ffffff;
    --blue:#1aa7e0;
    --blue-light:#6fd0f3;
    --green:#b4d334;
    --ink:#5d6770;
    --faint:#d7eef8;
  }
  *{margin:0;padding:0;box-sizing:border-box}
  html,body{width:1200px;height:936px;overflow:hidden;background:var(--bg);font-family:"Montserrat",Arial,sans-serif;color:var(--ink)}
  .canvas{position:relative;width:1200px;height:936px}
  .sheet{position:absolute;background:var(--paper);overflow:hidden}
  .sheet svg.wave{position:absolute;left:0;bottom:0;width:100%}
  .brand{display:flex;align-items:center;gap:8px;color:var(--blue);font-weight:700;white-space:nowrap;letter-spacing:.02em;text-transform:uppercase}
  .brand .dot{border-radius:50%;background:var(--blue);flex:none}
  .website{position:absolute;left:0;right:0;text-align:center;font-size:11px;letter-spacing:.18em;color:var(--blue);white-space:nowrap}
  .website.on-blue{color:#fff}

  /* letterhead */
  .letterhead{left:177px;top:63px;width:400px;height:562px}
  .letterhead .brand{position:absolute;left:18px;top:34px;font-size:16px}
  .letterhead .brand .dot{width:22px;height:22px}
  .letterhead .contact{position:absolute;left:270px;top:24px;font-size:7px;line-height:11px;white-space:nowrap}
  .letterhead .contact li{list-style:none;display:flex;align-items:center;gap:4px}
  .letterhead .contact li::before{content:"";width:5px;height:5px;border-radius:50%;background:var(--blue)}
  .letterhead .faint-mark{position:absolute;left:0;right:0;top:238px;text-align:center;font-size:26px;font-weight:700;color:var(--faint);text-transform:uppercase;letter-spacing:.04em;white-space:nowrap}
  .letterhead .website{bottom:22px}

  /* folder */
  .folder{left:633px;top:50px;width:460px;height:638px}
  .folder .brand{position:absolute;left:0;right:0;top:188px;justify-content:center;font-size:34px;gap:14px}
  .folder .brand .dot{width:46px;height:46px}
  .folder .website{bottom:24px;font-size:12px}

  /* business cards */
  .card{left:81px;width:172px;height:92px}
  .card-front{top:653px}
  .card-front .brand{position:absolute;left:8px;top:10px;font-size:9px;gap:4px}
  .card-front .brand .dot{width:11px;height:11px}
  .card-front .details{position:absolute;left:10px;top:34px;font-size:4.5px;line-height:6.5px;white-space:nowrap}
  .card-back{top:772px;height:96px;background:linear-gradient(160deg,var(--blue-light),var(--blue))}
  .card-back .back-name{position:absolute;left:0;right:0;top:40px;text-align:center;color:#fff;font-weight:700;font-size:10px;letter-spacing:.06em;text-transform:uppercase;opacity:.9;white-space:nowrap}
  .card-back .website{bottom:6px;font-size:5px}

  /* envelopes */
  .envelope-front{left:266px;top:738px;width:367px;height:162px}
  .envelope-front .brand{position:absolute;left:14px;top:16px;font-size:12px;gap:6px}
  .envelope-front .brand .dot{width:16px;height:16px}
  .envelope-front .city{position:absolute;left:14px;top:42px;font-size:7px;white-space:nowrap}
  .envelope-back{left:663px;top:741px;width:443px;height:165px;border:1px solid #e3e6e8}
  .envelope-back .website{top:16px;font-size:9px}
</style>
</head>
<body>
<div class="canvas">

  <section class="sheet letterhead">
    <div class="brand"><span class="dot"></span>Carla Venhuizen</div>
    <ul class="contact">
      <li>Marrowfield, CO</li>
      <li>(303) 555-0142</li>
      <li>carla.venhuizen@postvexa.com</li>
      <li>www.venhuizencoach.com</li>
    </ul>
    <div class="faint-mark">Carla Venhuizen</div>
    <svg class="wave" viewBox="0 0 400 80" height="80" preserveAspectRatio="none">
      <defs>
        <linearGradient id="lhGreen" x1="0" x2="1"><stop offset="0" stop-color="#6fd0f3"/><stop offset=".5" stop-color="#b4d334"/><stop offset="1" stop-color="#6fd0f3"/></linearGradient>
        <linearGradient id="lhBlue" x1="0" x2="1"><stop offset="0" stop-color="#3cb6e6"/><stop offset="1" stop-color="#1aa7e0"/></linearGradient>
      </defs>
      <path d="M0 22 C120 0 260 0 400 18 L400 30 C260 10 120 12 0 34Z" fill="url(#lhGreen)"/>
      <path d="M0 30 C120 14 260 16 400 28 L400 44 C260 32 120 34 0 46Z" fill="url(#lhBlue)"/>
    </svg>
    <div class="website">www.venhuizencoach.com</div>
  </section>

  <section class="sheet folder">
    <div class="brand"><span class="dot"></span>Carla Venhuizen</div>
    <svg class="wave" viewBox="0 0 460 150" height="150" preserveAspectRatio="none">
      <defs>
        <linearGradient id="fGreen" x1="0" x2="1"><stop offset="0" stop-color="#6fd0f3"/><stop offset=".55" stop-color="#b4d334"/><stop offset="1" stop-color="#6fd0f3"/></linearGradient>
        <linearGradient id="fBlue" x1="0" x2="0" y1="0" y2="1"><stop offset="0" stop-color="#4cc0ec"/><stop offset="1" stop-color="#1aa7e0"/></linearGradient>
      </defs>
      <path d="M0 38 C140 4 300 0 460 24 L460 40 C300 16 140 20 0 54Z" fill="url(#fGreen)"/>
      <path d="M0 54 C140 22 300 20 460 40 L460 150 L0 150Z" fill="url(#fBlue)"/>
    </svg>
    <div class="website on-blue">www.venhuizencoach.com</div>
  </section>

  <section class="sheet card card-front">
    <div class="brand"><span class="dot"></span>Carla Venhuizen</div>
    <div class="details">
      Success Coach &amp; Speaker<br>
      (303) 555-0142<br>
      carla.venhuizen@postvexa.com
    </div>
    <svg class="wave" viewBox="0 0 172 26" height="26" preserveAspectRatio="none">
      <path d="M0 12 C60 2 120 2 172 8 L172 12 C120 6 60 8 0 16Z" fill="#b4d334"/>
      <path d="M0 16 C60 8 120 8 172 12 L172 26 L0 26Z" fill="#1aa7e0"/>
    </svg>
  </section>

  <section class="sheet card card-back">
    <div class="back-name">Carla Venhuizen</div>
    <div class="website on-blue">www.venhuizencoach.com</div>
  </section>

  <section class="sheet envelope-front">
    <div class="brand"><span class="dot"></span>Carla Venhuizen</div>
    <div class="city">Marrowfield, CO</div>
  </section>

  <section class="sheet envelope-back">
    <svg viewBox="0 0 443 60" width="443" height="60" preserveAspectRatio="none" style="position:absolute;left:0;top:0">
      <defs>
        <linearGradient id="flap" x1="0" x2="0" y1="0" y2="1"><stop offset="0" stop-color="#4cc0ec"/><stop offset="1" stop-color="#1aa7e0"/></linearGradient>
      </defs>
      <path d="M0 0 L443 0 L443 34 C300 54 150 54 0 34Z" fill="url(#flap)"/>
    </svg>
    <div class="website on-blue">www.venhuizencoach.com</div>
  </section>

</div>
</body>
</html>
```